Corporate ppt for clients and partners /knowledge in German is important

We need to better design our ppt's that are used to present our firm to clients. Attached is the version that we currently use to explain our services to potential clients.
I would like to see a design that communicates clarity, integrity and uniqueness.

```html
<!DOCTYPE html>
<html lang="de">
<head>
<meta charset="utf-8">
<title>Nordlicht Security – Präsentationsvorlage</title>
<link href="https://fonts.googleapis.com/css2?family=Open+Sans:wght@400;600;700&display=swap" rel="stylesheet">
<style>
:root{
  --bg:#4a4343;--blue:#1e8fe6;--blue-dark:#1d4fa6;--navy:#24426e;--ink:#222;
  --grey:#8a8a8a;--light:#d9e2ee;--green:#5c9e2e;--orange:#f0642a;--lime:#8cc63f;
}
*{box-sizing:border-box;margin:0;padding:0}
html,body{width:1200px;height:1080px;overflow:hidden;background:var(--bg)}
.canvas{position:relative;width:1200px;height:1080px;background:var(--bg);font-family:'Open Sans',sans-serif}
.slide{position:absolute;width:290px;height:205px;background:#fff;overflow:hidden;color:var(--ink)}
.abs{position:absolute}
.title{position:absolute;left:14px;top:10px;font-size:9.5px;font-weight:700;color:var(--blue);text-transform:uppercase;letter-spacing:.2px}
.title::before{content:"";position:absolute;left:-14px;top:-2px;width:3px;height:14px;background:var(--blue)}
.title .dark{color:var(--blue-dark)}
.title-rule{position:absolute;left:14px;top:24px;width:228px;height:1px;background:linear-gradient(90deg,var(--blue),var(--light))}
.subtitle{position:absolute;left:14px;top:29px;font-size:5.5px;color:#333}
.brand{position:absolute;right:10px;top:4px;display:flex;align-items:center;gap:3px;font-size:5px;line-height:1.05;color:var(--navy);font-weight:600}
.brand-dot{width:10px;height:10px;border-radius:50%;background:var(--blue)}
.brand.on-dark{color:#fff}.brand.on-dark .brand-dot{background:#fff}
.footer{position:absolute;left:0;right:0;bottom:0;height:10px}
.footer .conf{position:absolute;left:14px;bottom:2px;font-size:5.5px;color:#222}
.footer .band{position:absolute;left:92px;right:0;bottom:0;height:6px;background:var(--blue);font-size:3.4px;color:#fff;padding-left:10px;line-height:6px}
.footer .page{position:absolute;right:0;bottom:0;width:38px;height:9px;background:var(--blue-dark);font-size:5.5px;color:#fff;text-align:center;line-height:9px}
.ph{position:absolute}
.small{font-size:4px;line-height:1.45;color:var(--grey)}
.body{font-size:5.2px;line-height:1.35;color:#333}
.strong{font-weight:700;color:#111}
.icon-box{position:absolute;width:16px;height:16px;border-radius:2px;display:flex;align-items:center;justify-content:center}
.toc-item{display:flex;gap:4px}
.toc-num{background:var(--blue);color:#fff;font-size:4.5px;width:12px;height:10px;text-align:center;line-height:10px;flex:none}
.member-photo{height:58px;background:linear-gradient(#6c7c6a,#2f3a30)}
</style>
</head>
<body>
<div class="canvas">

<!-- 1 Cover -->
<section class="slide" style="left:9px;top:9px">
  <div class="brand" style="left:28px;right:auto;top:20px;font-size:7px"><span class="brand-dot" style="width:16px;height:16px"></span><span>Nordlicht<br>Security</span></div>
  <div class="ph" role="img" aria-label="Leuchtturm auf Felsenküste in Graustufen" style="left:0;top:72px;width:146px;height:96px;background:linear-gradient(160deg,#cfd5dc,#7b8590 60%,#4d5560)"></div>
  <div class="abs" style="left:146px;top:72px;width:144px;height:96px;background:var(--blue);padding:24px 0 0 14px;color:#fff">
    <div style="font-size:12px;letter-spacing:.3px">TEMPLATE <span style="font-weight:700">TITLE</span></div>
    <div style="font-size:5.5px;margin-top:6px">SUB-TITLE HERE</div>
    <div style="font-size:3.4px;margin-top:18px">© 2015 Nordlicht Security | Ihre IT-Sicherheits-Analysten</div>
  </div>
</section>

<!-- 2 Title dark -->
<section class="slide" style="left:307px;top:9px;background:var(--navy)">
  <div class="ph" role="img" aria-label="Küstenlandschaft mit Leuchtturm in dunklem Blau" style="inset:0;background:radial-gradient(ellipse at 50% 80%,#3a5785,#1e3458 70%)"></div>
  <div class="brand on-dark" style="left:122px;right:auto;top:38px;font-size:6px"><span class="brand-dot" style="width:14px;height:14px"></span><span>Nordlicht<br>Security</span></div>
  <div class="abs" style="left:0;right:0;top:102px;text-align:center;color:#fff">
    <div style="font-size:11px;letter-spacing:.3px">POWERPOINT TEMPLATE</div>
    <div style="font-size:8.5px;font-weight:700;margin-top:3px">TITLE HERE</div>
    <div style="font-size:5px;margin-top:6px">SUB-TITLE HERE</div>
  </div>
  <div class="abs" style="left:0;right:0;bottom:5px;text-align:center;font-size:3.4px;color:#fff">© 2015 Nordlicht Security | Ihre IT-Sicherheits-Analysten</div>
  <div class="abs" style="left:112px;bottom:1px;width:66px;height:2px;background:var(--blue)"></div>
</section>

<!-- 3 Content table -->
<section class="slide" style="left:606px;top:9px">
  <div class="title">Content Table</div><div class="title-rule"></div><div class="subtitle">SUB-TITLE HERE</div>
  <div class="brand"><span class="brand-dot"></span><span>Nordlicht<br>Security</span></div>
  <div class="abs" style="left:28px;top:50px;width:250px;display:grid;grid-template-columns:1fr 1fr;row-gap:10px;column-gap:10px">
    <div class="toc-item"><span class="toc-num">01</span><span class="body" style="font-size:5px">Lorem ipsum dolor sit amet,<br>consetetur sadipscing elitr.</span></div>
    <div class="toc-item"><span class="toc-num">01</span><span class="body" style="font-size:5px">Lorem ipsum dolor sit amet,<br>consetetur sadipscing elitr.</span></div>
    <div class="toc-item"><span class="toc-num">01</span><span class="body" style="font-size:5px">Lorem ipsum dolor sit amet,<br>consetetur sadipscing elitr.</span></div>
    <div class="toc-item"><span class="toc-num">01</span><span class="body" style="font-size:5px">Lorem ipsum dolor sit amet,<br>consetetur sadipscing elitr.</span></div>
    <div class="toc-item"><span class="toc-num">01</span><span class="body" style="font-size:5px">Lorem ipsum dolor sit amet,<br>consetetur sadipscing elitr.</span></div>
    <div class="toc-item"><span class="toc-num">01</span><span class="body" style="font-size:5px">Lorem ipsum dolor sit amet,<br>consetetur sadipscing elitr.</span></div>
    <div class="toc-item"><span class="toc-num">01</span><span class="body" style="font-size:5px">Lorem ipsum dolor sit amet,<br>consetetur sadipscing elitr.</span></div>
    <div class="toc-item"><span class="toc-num">01</span><span class="body" style="font-size:5px">Lorem ipsum dolor sit amet,<br>consetetur sadipscing elitr.</span></div>
    <div class="toc-item"><span class="toc-num">01</span><span class="body" style="font-size:5px">Lorem ipsum dolor sit amet,<br>consetetur sadipscing elitr.</span></div>
  </div>
  <div class="footer"><span class="conf">confidential</span><div class="band">© 2015 Nordlicht Security | Ihre IT-Sicherheits-Analysten</div><div class="page">Page 01</div></div>
</section>

<!-- 4 Welcome -->
<section class="slide" style="left:904px;top:9px;background:var(--blue)">
  <div class="abs" style="left:0;right:0;top:103px;height:102px;background:var(--blue-dark)"></div>
  <div class="abs" style="left:0;right:0;top:17px;text-align:center;color:#fff;font-size:9.5px;font-weight:700">WELCOME MESSAGE</div>
  <div class="abs" style="left:40px;right:40px;top:50px;text-align:center;color:#fff;font-size:4.8px;line-height:1.4">Duis autem vel eum iriure dolor in hendrerit in vulputate velit esse molestie consequat, vel illum dolore eu feugiat nulla facilisis.</div>
  <div class="ph" role="img" aria-label="Porträtfoto eines Mitarbeiters" style="left:117px;top:78px;width:56px;height:56px;border-radius:50%;background:radial-gradient(circle,#8a7a6c,#3c3a3a);border:2px solid #fff"></div>
  <div class="abs" style="left:18px;right:18px;top:142px;text-align:center;color:#fff;font-size:4.8px;line-height:1.45"><b style="font-size:8px">“</b> Lorem ipsum dolor sit amet, consetetur sadipscing elitr, sed diam nonumy eirmod tempor invidunt ut labore et dolore magna aliquyam erat, sed diam voluptua. At vero eos et accusam et justo duo dolores et ea rebum.</div>
  <div class="footer"><span class="conf" style="color:#fff">confidential</span><div class="band">© 2015 Nordlicht Security | Ihre IT-Sicherheits-Analysten</div><div class="page">Page 01</div></div>
</section>

<!-- 5 Wer wir sind -->
<section class="slide" style="left:9px;top:221px">
  <div class="title">Wer wir sind</div><div class="title-rule"></div><div class="subtitle">SUB-TITLE HERE</div>
  <div class="brand"><span class="brand-dot"></span><span>Nordlicht<br>Security</span></div>
  <div class="abs body strong" style="left:22px;top:45px;width:140px;font-size:5.3px;line-height:1.25">Nordlicht Security ist ein führendes Unternehmen auf dem Gebiet umfassender Sicherheitsanalysen und zielgerichteter Penetration Tests</div>
  <div class="abs small" style="left:22px;top:78px;width:140px;font-size:3.6px">Wir bieten Ihnen qualitativ hochwertige und umfassende Penetration Tests im gesamten IT-Umfeld. Unsere Sicherheitsanalysten sind allesamt renommierte Experten mit dem entsprechenden Wissen sowie der nötigen Erfahrung bei manuellen Vorgehen und helfen Ihnen Ihre kritische IT-Infrastruktur, mögliche Web-Applikationen, eigene Software-Programmierung oder auch das Sicherheitsbewusstsein Ihrer Mitarbeiter stark zu verbessern. Unsere permanenten Recherchen und Entwicklungen im eigenen Forschungslabor geben uns, gegenüber der wachsenden Cyber-Kriminalität, einen entscheidenden Wissensvorsprung. Diese Pionierarbeit können wir Ihnen auch in Form von individuellen Workshops und Schulungen gerne weiter vermitteln. Generell wahren wir durch unsere Fokussierung auf Penetration Tests die nötige Neutralität und Objektivität und stellen die gesicherte Unbefangenheit unserer Ergebnisse sowie Empfehlungen sicher.</div>
  <div class="ph" role="img" aria-label="Modernes Großraumbüro in Blaugrau" style="left:176px;top:44px;width:100px;height:142px;background:linear-gradient(170deg,#dfe6ee,#8e9bab 55%,#5f6b78)"></div>
  <div class="footer"><span class="conf">confidential</span><div class="band">© 2015 Nordlicht Security | Ihre IT-Sicherheits-Analysten</div><div class="page">Page 01</div></div>
</section>

<!-- 6 Our team -->
<section class="slide" style="left:307px;top:221px">
  <div class="title">Our Team</div><div class="title-rule"></div><div class="subtitle">SUB-TITLE HERE</div>
  <div class="brand"><span class="brand-dot"></span><span>Nordlicht<br>Security</span></div>
  <div class="abs" style="left:24px;top:53px;width:248px;display:grid;grid-template-columns:repeat(4,1fr);column-gap:22px;text-align:center">
    <div><div class="member-photo" role="img" aria-label="Teamfoto Lukas Berger"></div><div style="font-size:5px;color:var(--blue-dark);margin-top:3px">Lukas Berger</div><div style="font-size:3px;color:var(--grey)">Founder / CEO</div><div style="font-size:4.5px;color:var(--blue-dark);font-weight:600;margin-top:3px">Experience</div><div class="small" style="font-size:3.2px">Lorem ipsum dolor sit amet, consetetur elitr, ut blandit nunc at.</div></div>
    <div><div class="member-photo" role="img" aria-label="Teamfoto Anna Weiss"></div><div style="font-size:5px;color:var(--blue);margin-top:3px">Anna Weiss</div><div style="font-size:3px;color:var(--grey)">Founder / COO</div><div style="font-size:4.5px;color:var(--blue-dark);font-weight:600;margin-top:3px">Experience</div><div class="small" style="font-size:3.2px">Lorem ipsum dolor sit amet, consetetur elitr, ut blandit nunc at.</div></div>
    <div><div class="member-photo" role="img" aria-label="Teamfoto Tobias Krahn"></div><div style="font-size:5px;color:var(--blue-dark);margin-top:3px">Tobias Krahn</div><div style="font-size:3px;color:var(--grey)">Account Manager</div><div style="font-size:4.5px;color:var(--blue-dark);font-weight:600;margin-top:3px">Experience</div><div class="small" style="font-size:3.2px">Lorem ipsum dolor sit amet, consetetur elitr, ut blandit nunc at.</div></div>
    <div><div class="member-photo" role="img" aria-label="Teamfoto Miriam Vogt"></div><div style="font-size:5px;color:var(--blue);margin-top:3px">Miriam Vogt</div><div style="font-size:3px;color:var(--grey)">Sales Executive</div><div style="font-size:4.5px;color:var(--blue-dark);font-weight:600;margin-top:3px">Experience</div><div class="small" style="font-size:3.2px">Lorem ipsum dolor sit amet, consetetur elitr, ut blandit nunc at.</div></div>
  </div>
  <div class="footer"><span class="conf">confidential</span><div class="band">© 2015 Nordlicht Security | Ihre IT-Sicherheits-Analysten</div><div class="page">Page 01</div></div>
</section>

<!-- 7 Was wir machen -->
<section class="slide" style="left:606px;top:221px">
  <div class="title">Was wir machen</div><div class="title-rule"></div><div class="subtitle">SUB-TITLE HERE</div>
  <div class="brand"><span class="brand-dot"></span><span>Nordlicht<br>Security</span></div>
  <div class="ph" role="img" aria-label="Weltkarte mit Hand auf Touchscreen in Blautönen" style="left:0;top:38px;width:290px;height:86px;background:linear-gradient(90deg,#2b5a9a,#3a78c0 45%,#4f7fb4 75%,#7d8ea6)"></div>
  <div class="abs" style="left:10px;right:10px;top:88px;display:grid;grid-template-columns:repeat(4,1fr);text-align:center">
    <div><div style="font-size:4.3px;color:#fff;height:18px">PENETRATION TEST</div><div style="margin:4px auto 0;width:20px;height:20px;background:var(--blue);border:1px solid #fff"></div><div class="small" style="font-size:3.8px;margin-top:4px">Penetrationstests und Sicherheitsberatung</div></div>
    <div><div style="font-size:4.3px;color:#fff;height:18px">APPLIKATIONS<br>SICHERHEIT</div><div style="margin:4px auto 0;width:20px;height:20px;background:var(--green);border:1px solid #fff"></div><div class="small" style="font-size:3.8px;margin-top:4px">Reverse Engineering &amp; Source Code Review</div></div>
    <div><div style="font-size:4.3px;color:#fff;height:18px">FORSCHUNG &amp;<br>ENTWICKLUNG</div><div style="margin:4px auto 0;width:20px;height:20px;background:var(--blue);border:1px solid #fff"></div><div class="small" style="font-size:3.8px;margin-top:4px">Eigenes IT-Forschungslabor zur Kompetenzsicherung</div></div>
    <div><div style="font-size:4.3px;color:#fff;height:18px">SCHULUNGEN</div><div style="margin:4px auto 0;width:20px;height:20px;background:var(--orange);border:1px solid #fff"></div><div class="small" style="font-size:3.8px;margin-top:4px">Schulungen, Workshops, individuelle Trainings und Coaching</div></div>
  </div>
  <div class="footer"><span class="conf">confidential</span><div class="band">© 2015 Nordlicht Security | Ihre IT-Sicherheits-Analysten</div><div class="page">Page 01</div></div>
</section>

<!-- 8 Penetration tests -->
<section class="slide" style="left:904px;top:221px">
  <div class="title">Beispiele: <span class="dark">Penetration Tests</span></div><div class="title-rule"></div><div class="subtitle">SUB-TITLE HERE</div>
  <div class="brand"><span class="brand-dot"></span><span>Nordlicht<br>Security</span></div>
  <div class="icon-box" style="left:24px;top:50px;width:22px;height:22px;background:var(--blue)"><svg width="14" height="14" viewBox="0 0 14 14" fill="none" stroke="#fff" stroke-width="1"><circle cx="7" cy="7" r="6"/><circle cx="7" cy="7" r="3.5"/><circle cx="7" cy="7" r="1"/></svg></div>
  <div class="abs body" style="left:52px;top:50px;width:226px;font-size:5px;line-height:1.4"><span class="strong">Ein Penetration Test ist ein komplexer Prozess.</span><br><u>Hier gilt die Devise</u>: <i>Ihr Analyst muss so gut sein, wie der potentielle Angreifer. Daher setzt Nordlicht Security auf eine manuelle Vorgehensweise und überlässt nichts dem Zufall.</i></div>
  <ul class="abs" style="left:52px;top:88px;list-style:none;font-size:5.6px;line-height:1.65;color:var(--grey)">
    <li><span style="color:var(--blue)">●</span> Web-Applikationen</li><li><span style="color:var(--blue)">●</span> SCADA Steuerungssysteme</li><li><span style="color:var(--blue)">●</span> Social Engineering</li><li><span style="color:var(--blue)">●</span> Mobile/MDM Sicherheit Tests</li><li><span style="color:var(--blue)">●</span> PCI-DSS Tests</li><li><span style="color:var(--blue)">●</span> VoIP Tests</li><li><span style="color:var(--blue)">●</span> Collaboration-Server Tests</li><li><span style="color:var(--blue)">●</span> ERP-System Penetration Tests</li><li><span style="color:var(--blue)">●</span> ATM Security Analysen</li><li><span style="color:var(--blue)">●</span> Remote-Desktop “Break Out” Penetration Tests</li>
  </ul>
  <div class="footer"><span class="conf">confidential</span><div class="band">© 2015 Nordlicht Security | Ihre IT-Sicherheits-Analysten</div><div class="page">Page 01</div></div>
</section>

<!-- 9 Section break -->
<section class="slide" style="left:9px;top:437px">
  <div class="ph" role="img" aria-label="Person mit Kapuze vor Laptop in dunklem Grau" style="left:117px;top:0;width:173px;height:205px;background:linear-gradient(200deg,#6e7378,#2b2e33 60%,#9aa0a6)"></div>
  <div class="abs" style="left:0;top:0;width:117px;height:205px;background:var(--blue)"></div>
  <div class="abs" style="left:16px;top:90px;color:#fff"><div style="font-size:9.5px;font-weight:700">SECTION BREAK</div><div style="font-size:3.6px;margin-top:4px;width:80px;line-height:1.4">Lorem ipsum dolor sit amet, consetetur sadipscing elitr.</div><div style="margin-top:6px;width:30px;height:2px;background:#fff"></div></div>
  <div class="brand on-dark" style="top:10px"><span class="brand-dot" style="width:14px;height:14px"></span><span style="font-size:6px">Nordlicht<br>Security</span></div>
</section>

<!-- 10 IT-Security Lab -->
<section class="slide" style="left:307px;top:437px">
  <div class="title">Beispiele: <span class="dark">IT-Security Lab</span></div><div class="title-rule"></div><div class="subtitle">SUB-TITLE HERE</div>
  <div class="brand"><span class="brand-dot"></span><span>Nordlicht<br>Security</span></div>
  <div class="icon-box" style="left:24px;top:46px;width:22px;height:22px;background:var(--lime)"><svg width="13" height="13" viewBox="0 0 13 13" fill="none" stroke="#fff" stroke-width="1.6"><circle cx="5" cy="5" r="3.6"/><path d="M8 8l4 4"/></svg></div>
  <div class="abs body strong" style="left:52px;top:47px;width:225px;font-size:5.1px;line-height:1.25">Wir führen Forschungsprojekte zu aufkommenden und aktuellen Trends und Technologien in unserem eigenen Security Lab durch:</div>
  <div class="abs" style="left:60px;top:78px;width:220px;font-size:4.3px;line-height:1.35;color:var(--grey)">
    <div><span style="color:var(--lime)">►</span> Schwachstellenanalyse verbreiteter Hard- und Software (“Responsible Disclosure”)</div>
    <div style="margin:5px 0 0 12px"><span style="color:var(--lime)">►</span> Demonstration der Ausnutzbarkeit von Schwachstellen</div>
    <div style="margin-top:5px"><span style="color:var(--lime)">►</span> Entwicklung eigener Tools zur Identifizierung neuer Schwachstellen bzw. um Sicherheitsanalysen in Spezialbereichen erst zu ermöglichen</div>
    <div style="margin-top:5px"><span style="color:var(--lime)">►</span> Erforschung aufkommender Technologien und Veröffentlichung der Forschungsergebnisse in Form von Papers und Präsentationen</div>
  </div>
  <div class="abs body" style="left:52px;top:139px;width:228px;font-size:5px;line-height:1.3;color:#222">Wir führen auch Forschungsprojekte im Kundenauftrag durch. Wird ein kritischer Pfeiler Ihrer Unternehmenssicherheit zukünftig auf einem Produkt oder einer bestimmten Technologie basieren? Wir finden heraus, wo die Schwachstellen von morgen liegen werden und geben Ihnen bereits heute Handlungsempfehlungen.</div>
  <div class="footer"><span class="conf">confidential</span><div class="band">© 2015 Nordlicht Security | Ihre IT-Sicherheits-Analysten</div><div class="page">Page 01</div></div>
</section>

<!-- 11 Applikationssicherheit -->
<section class="slide" style="left:606px;top:437px">
  <div class="title">Beispiele: <span class="dark">Applikationssicherheit</span></div><div class="title-rule"></div><div class="subtitle">SUB-TITLE HERE</div>
  <div class="brand"><span class="brand-dot"></span><span>Nordlicht<br>Security</span></div>
  <div class="icon-box" style="left:24px;top:46px;width:22px;height:22px;background:var(--green)"><svg width="14" height="14" viewBox="0 0 14 14" fill="none" stroke="#fff" stroke-width="1"><circle cx="7" cy="7" r="6"/><path d="M1 7h12M7 1c3 3 3 9 0 12M7 1c-3 3-3 9 0 12"/></svg></div>
  <div class="abs small" style="left:58px;top:45px;width:222px;font-size:4.9px;line-height:1.3">Mit dem Ziel eines gegen externe Angriffe und interne Risiken abgesicherten IT-Systems, unterziehen wir Software und Applikationen jeglicher Art einer Sicherheitsanalyse. Dabei können sowohl Webapplikationen, Client-Server-Anwendungen, Plugins &amp; Addons oder auch die Firmware eines Embedded Systems betrachtet werden.</div>
  <div class="ph" role="img" aria-label="Geschäftsmann mit Datenmuster in Blau" style="left:32px;top:96px;width:82px;height:82px;border-radius:50%;background:radial-gradient(circle at 45% 40%,#a9c2dc,#4d6f97 70%)"></div>
  <svg class="abs" style="left:110px;top:100px" width="80" height="80" viewBox="0 0 80 80" fill="none" stroke="#1d4fa6" stroke-width=".6"><path d="M4 40L78 4M6 40H78M4 40L78 76"/></svg>
  <div class="abs" style="left:184px;top:98px;display:flex;flex-direction:column;gap:20px;font-size:4.8px;font-weight:700">
    <div style="display:flex;align-items:center;gap:6px"><span style="width:14px;height:14px;background:var(--blue);border-radius:2px 2px 7px 7px"></span>Source Code Review</div>
    <div style="display:flex;align-items:center;gap:6px"><span style="width:14px;height:14px;background:var(--blue-dark);border-radius:2px 2px 7px 7px"></span>Reverse Engineering</div>
    <div style="display:flex;align-items:center;gap:6px"><span style="width:14px;height:14px;background:var(--blue-dark);border-radius:2px 2px 7px 7px"></span>Malware Analyse</div>
  </div>
  <div class="footer"><span class="conf">confidential</span><div class="band">© 2015 Nordlicht Security | Ihre IT-Sicherheits-Analysten</div><div class="page">Page 01</div></div>
</section>

<!-- 12 Schulungen -->
<section class="slide" style="left:904px;top:437px">
  <div class="title">Beispiele: <span class="dark">Schulungen</span></div><div class="title-rule"></div><div class="subtitle">SUB-TITLE HERE</div>
  <div class="brand"><span class="brand-dot"></span><span>Nordlicht<br>Security</span></div>
  <svg class="abs" style="left:30px;top:60px" width="100" height="120" viewBox="0 0 100 120"><path d="M32 60L68 20M32 60L68 100" stroke="#1d4fa6" stroke-width=".7"/><circle cx="32" cy="60" r="24" fill="#f0642a"/><path d="M22 50h14v4h-10v14h14v-8h4v12H22z" fill="#fff"/><path d="M30 66l2-7 12-12 5 5-12 12z" fill="#fff"/><circle cx="68" cy="20" r="14" fill="#1e8fe6"/><circle cx="63" cy="20" r="2.5" fill="#fff"/><circle cx="73" cy="20" r="2.5" fill="#fff"/><circle cx="68" cy="16" r="2.5" fill="#fff"/><circle cx="68" cy="100" r="14" fill="#1d4fa6"/><ellipse cx="68" cy="99" rx="7" ry="5" fill="#fff"/></svg>
  <div class="abs" style="left:146px;top:52px;width:130px">
    <div style="font-size:5px;font-weight:700">ABWEHR VON SOCIAL ENGINEERING</div>
    <div class="small" style="font-size:3.3px;margin-top:3px">• Als Einfallstor in ein Unternehmen werden heutzutage zu 50% Social-Engineering-Attacken verwendet. Deshalb sehen wir dieses Modul als eine absolute Notwendigkeit an.<br>• Mit diesem Modul schulen wir die Mitarbeiter unserer Kunden, Social-Engineering-Angriffe aufzudecken und Gegenmaßnahmen einzuleiten.<br>• Anhand von realen Fallbeispielen lernen die Mitarbeiter, welche Informationen ein Angreifer nutzen kann.</div>
    <div style="font-size:5px;font-weight:700;margin-top:24px">WORKSHOP PENETRATION TESTS</div>
    <div class="small" style="font-size:3.3px;margin-top:3px">Workshop für angehende Penetrationstester, der die Grundlagen und Vorgehensweisen zur Durchführung eigener Pen-Tests vermittelt.</div>
  </div>
  <div class="footer"><span class="conf">confidential</span><div class="band">© 2015 Nordlicht Security | Ihre IT-Sicherheits-Analysten</div><div class="page">Page 01</div></div>
</section>

<!-- 13 Begleiter -->
<section class="slide" style="left:9px;top:651px">
  <div class="title" style="font-size:6.5px;line-height:1.25;top:9px">Nordlicht Security –<br><span class="dark">Ihr Begleiter zum Schutz Ihrer Daten</span></div><div class="title-rule" style="top:25px"></div><div class="subtitle" style="top:30px">SUB-TITLE HERE</div>
  <div class="brand"><span class="brand-dot"></span><span>Nordlicht<br>Security</span></div>
  <div class="ph" role="img" aria-label="Händedruck vor Geschäftsleuten" style="left:24px;top:55px;width:126px;height:126px;border-radius:50%;background:radial-gradient(circle at 40% 50%,#f1e6dc,#9fb4cc 55%,#dfe8f2 80%)"></div>
  <div class="abs small" style="right:16px;top:55px;width:120px;text-align:right;font-size:4.9px;line-height:1.35">Für eine persönliche und erste vertrauliche Detailanalyse setzen Sie sich einfach mit uns in Verbindung. Bei einem gemeinsamen Treffen mit unserem Expertenteam können wir Sie bei allen hier angeführten Fragen eingehend beraten.</div>
  <div class="abs" style="right:16px;top:123px;font-size:5px;font-weight:700;color:var(--blue-dark)">GEHEN SIE AUF NUMMER SICHER!</div>
  <div class="abs" style="right:16px;top:139px;font-size:5px;color:#222">Wir danken für Ihre Aufmerksamkeit.</div>
  <div class="footer"><span class="conf">confidential</span><div class="band">© 2015 Nordlicht Security | Ihre IT-Sicherheits-Analysten</div><div class="page">Page 01</div></div>
</section>

<!-- 14 Donut chart -->
<section class="slide" style="left:307px;top:651px">
  <div class="title">Chart Slide</div><div class="title-rule"></div><div class="subtitle">SUB-TITLE HERE</div>
  <div class="brand"><span class="brand-dot"></span><span>Nordlicht<br>Security</span></div>
  <svg class="abs" style="left:40px;top:68px" width="90" height="90" viewBox="0 0 90 90">
    <g transform="rotate(-90 45 45)" fill="none" stroke-width="16">
      <circle cx="45" cy="45" r="26" stroke="#29a8ef" stroke-dasharray="24.5 163.4"/>
      <circle cx="45" cy="45" r="26" stroke="#1d4fa6" stroke-dasharray="32.7 163.4" stroke-dashoffset="-24.5"/>
      <circle cx="45" cy="45" r="26" stroke="#1e8fe6" stroke-dasharray="40.8 163.4" stroke-dashoffset="-57.2"/>
      <circle cx="45" cy="45" r="26" stroke="#24528f" stroke-dasharray="65.4 163.4" stroke-dashoffset="-98"/>
    </g>
    <g fill="#fff" font-size="6" font-family="Open Sans,sans-serif" font-weight="700" text-anchor="middle"><text x="60" y="24">15%</text><text x="72" y="56">20%</text><text x="45" y="82">25%</text><text x="16" y="48">40%</text></g>
  </svg>
  <div class="abs" style="left:160px;top:64px;display:flex;flex-direction:column;gap:8px">
    <div style="display:flex;gap:4px"><span style="width:12px;height:12px;border-radius:50%;background:var(--blue-dark);flex:none"></span><div><div style="font-size:3.6px;font-weight:700;color:var(--blue-dark)">TITLE GOES HERE</div><div class="small" style="font-size:3px;width:76px">There are many variations of passages of lorem ipsum available.</div></div></div>
    <div style="display:flex;gap:4px"><span style="width:12px;height:12px;border-radius:50%;background:var(--blue);flex:none"></span><div><div style="font-size:3.6px;font-weight:700;color:var(--blue-dark)">TITLE GOES HERE</div><div class="small" style="font-size:3px;width:76px">There are many variations of passages of lorem ipsum available.</div></div></div>
    <div style="display:flex;gap:4px"><span style="width:12px;height:12px;border-radius:50%;background:var(--blue-dark);flex:none"></span><div><div style="font-size:3.6px;font-weight:700;color:var(--blue-dark)">TITLE GOES HERE</div><div class="small" style="font-size:3px;width:76px">There are many variations of passages of lorem ipsum available.</div></div></div>
    <div style="display:flex;gap:4px"><span style="width:12px;height:12px;border-radius:50%;background:var(--blue);flex:none"></span><div><div style="font-size:3.6px;font-weight:700;color:var(--blue-dark)">TITLE GOES HERE</div><div class="small" style="font-size:3px;width:76px">There are many variations of passages of lorem ipsum available.</div></div></div>
  </div>
  <div class="footer"><span class="conf">confidential</span><div class="band">© 2015 Nordlicht Security | Ihre IT-Sicherheits-Analysten</div><div class="page">Page 01</div></div>
</section>

<!-- 15 Line chart -->
<section class="slide" style="left:606px;top:651px">
  <div class="title">Chart Slide</div><div class="title-rule"></div><div class="subtitle">SUB-TITLE HERE</div>
  <div class="brand"><span class="brand-dot"></span><span>Nordlicht<br>Security</span></div>
  <div class="abs" style="left:28px;top:45px;display:flex;gap:4px;align-items:center;font-size:3.8px"><span style="background:var(--blue);color:#fff;padding:1px 5px">Keyword</span>Discription / 2015 / May</div>
  <svg class="abs" style="left:0;top:54px" width="290" height="114" viewBox="0 48 290 114" font-family="Open Sans,sans-serif">
    <g stroke="#e3e7ec" stroke-width=".4"><path d="M30 70H282M30 82H282M30 94H282M30 106H282M30 118H282M30 130H282M30 142H282"/></g>
    <path d="M30 150H282" stroke="#999" stroke-width=".5"/>
    <g font-size="3.2" fill="#666" text-anchor="end"><text x="27" y="71">$100,00</text><text x="27" y="83">$80,00</text><text x="27" y="95">$70,00</text><text x="27" y="107">$50,00</text><text x="27" y="119">$30,00</text><text x="27" y="131">$20,00</text><text x="27" y="143">$10,00</text></g>
    <polyline fill="none" stroke="#9aa3ad" stroke-width=".7" points="32,134 40,121 48,128 57,108 65,115 73,95 81,102 89,111 98,89 106,92 114,98 122,82 130,95 139,102 147,105 155,108 163,98 171,103 180,95 188,89 196,92 204,85 212,82 221,78 229,74 237,77 245,69 253,66 262,64 270,61"/>
    <g fill="#1e8fe6"><circle cx="48" cy="128" r="2"/><circle cx="114" cy="98" r="2" fill="#1d4fa6"/><circle cx="155" cy="108" r="2"/><circle cx="245" cy="69" r="2" fill="#1d4fa6"/></g>
    <g fill="none" stroke-width="1.5"><circle cx="48" cy="120" r="3.5" stroke="#1e8fe6"/><circle cx="114" cy="90" r="3.5" stroke="#1d4fa6"/><circle cx="155" cy="100" r="3.5" stroke="#1e8fe6"/><circle cx="245" cy="61" r="3.5" stroke="#1d4fa6"/></g>
    <g font-size="6" font-weight="700" text-anchor="middle"><text x="48" y="113" fill="#1e8fe6">30$</text><text x="114" y="83" fill="#1d4fa6">50$</text><text x="155" y="93" fill="#1e8fe6">40$</text><text x="245" y="54" fill="#1d4fa6">70$</text></g>
    <g font-size="3" fill="#666" text-anchor="middle"><text x="32" y="156">1</text><text x="48" y="156">3</text><text x="65" y="156">5</text><text x="81" y="156">7</text><text x="98" y="156">9</text><text x="114" y="156">11</text><text x="130" y="156">13</text><text x="147" y="156">15</text><text x="163" y="156">17</text><text x="180" y="156">19</text><text x="196" y="156">21</text><text x="212" y="156">23</text><text x="229" y="156">25</text><text x="245" y="156">27</text><text x="262" y="156">29</text></g>
  </svg>
  <div class="abs" style="left:0;right:0;top:171px;text-align:center;font-size:4px;color:#333">TITLE GOES HERE</div>
  <div class="abs small" style="left:40px;right:40px;top:177px;text-align:center;font-size:3.1px;line-height:1.3">There are many variations of passages of Lorem Ipsum available, but the majority have suffered alteration in some form, by injected humour, or randomised words which don't look even slightly believable.</div>
  <div class="footer"><span class="conf">confidential</span><div class="band">© 2015 Nordlicht Security | Ihre IT-Sicherheits-Analysten</div><div class="page">Page 01</div></div>
</section>

<!-- 16 Bar charts -->
<section class="slide" style="left:904px;top:651px">
  <div class="title">Chart Slide</div><div class="title-rule"></div><div class="subtitle">SUB-TITLE HERE</div>
  <div class="brand"><span class="brand-dot"></span><span>Nordlicht<br>Security</span></div>
  <svg class="abs" style="left:0;top:58px" width="290" height="80" viewBox="0 0 290 80" font-family="Open Sans,sans-serif">
    <g font-size="3" fill="#666" text-anchor="end"><text x="20" y="6">120</text><text x="20" y="17">100</text><text x="20" y="28">80</text><text x="20" y="39">60</text><text x="20" y="50">40</text><text x="20" y="61">20</text><text x="20" y="72">0</text></g>
    <path d="M24 72H140M148 72H276" stroke="#bbb" stroke-width=".5"/>
    <g><rect x="36" y="17" width="6" height="55" fill="#1d4fa6"/><rect x="43" y="22" width="5" height="50" fill="#1e8fe6"/><rect x="64" y="22" width="6" height="50" fill="#1d4fa6"/><rect x="71" y="55" width="5" height="17" fill="#1e8fe6"/><rect x="92" y="26" width="6" height="46" fill="#1d4fa6"/><rect x="99" y="40" width="5" height="32" fill="#1e8fe6"/><rect x="120" y="17" width="6" height="55" fill="#1d4fa6"/><rect x="127" y="62" width="5" height="10" fill="#1e8fe6"/></g>
    <g><rect x="156" y="17" width="12" height="55" fill="#555"/><rect x="184" y="56" width="12" height="16" fill="#aaa"/><rect x="212" y="60" width="12" height="12" fill="#1d4fa6"/><rect x="240" y="66" width="12" height="6" fill="#1e8fe6"/></g>
    <g font-size="3" fill="#666" text-anchor="start"><text x="280" y="6">120</text><text x="280" y="28">80</text><text x="280" y="50">40</text><text x="280" y="72">0</text></g>
    <g font-size="3" fill="#666" text-anchor="middle"><text x="42" y="77">2010</text><text x="70" y="77">2012</text><text x="98" y="77">2014</text><text x="126" y="77">2016</text><text x="162" y="77">2016</text><text x="190" y="77">2010</text><text x="218" y="77">2012</text><text x="246" y="77">2016</text></g>
  </svg>
  <div class="abs" style="left:22px;top:146px;width:110px"><div style="font-size:4px;color:var(--blue-dark);font-weight:600">Description Here</div><div style="display:flex;gap:3px;align-items:center"><span style="font-size:9px;color:var(--blue)">80%</span><span class="small" style="font-size:2.8px">There are many of the variations passages have suffered</span></div><div class="small" style="font-size:2.8px">There are many variations of passages of Lorem Ipsum available, but the majority have suffered alteration.</div></div>
  <div class="abs" style="left:160px;top:146px;width:110px"><div style="font-size:4px;color:#222;font-weight:600">Description Here</div><div style="display:flex;gap:3px;align-items:center"><span style="font-size:9px;color:#333">20%</span><span class="small" style="font-size:2.8px">There are many of the variations passages have suffered</span></div><div class="small" style="font-size:2.8px">There are many variations of passages of Lorem Ipsum available, but the majority have suffered alteration.</div></div>
  <div class="footer"><span class="conf">confidential</span><div class="band">© 2015 Nordlicht Security | Ihre IT-Sicherheits-Analysten</div><div class="page">Page 01</div></div>
</section>

<!-- 17 Table -->
<section class="slide" style="left:9px;top:866px">
  <div class="title">Table Slide</div><div class="title-rule"></div><div class="subtitle">SUB-TITLE HERE</div>
  <div class="brand"><span class="brand-dot"></span><span>Nordlicht<br>Security</span></div>
  <table class="abs" style="left:12px;top:37px;width:266px;border-collapse:collapse;font-size:3.5px;font-family:Georgia,serif">
    <tr style="background:var(--blue);color:#fff;font-weight:700"><td style="padding:2px">First Topic</td><td>Number</td><td>Text title</td><td>Text title</td></tr>
    <tr style="border-bottom:.5px solid #ddd"><td style="padding:2px">Text</td><td>0.00</td><td>Text</td><td>Text</td></tr>
    <tr style="border-bottom:.5px solid #ddd"><td style="padding:2px">Text</td><td>0.00</td><td>Text</td><td>Text</td></tr>
    <tr style="background:#8fc6ee;color:#fff;font-weight:700"><td style="padding:2px">Second Topic</td><td>Number</td><td>Text title</td><td>Text title</td></tr>
    <tr style="border-bottom:.5px solid #ddd"><td style="padding:2px">Text</td><td>0.00</td><td>Text</td><td>Text</td></tr>
    <tr style="border-bottom:.5px solid #ddd"><td style="padding:2px">Text</td><td>0.00</td><td>Text</td><td>Text</td></tr>
    <tr style="background:#dbe9f6;border-bottom:.5px solid #ddd"><td style="padding:2px">Text</td><td>0.00</td><td>Text</td><td>Text</td></tr>
    <tr style="border-bottom:.5px solid #ddd"><td style="padding:2px">Text</td><td>0.00</td><td>Text</td><td>Text</td></tr>
  </table>
  <div class="abs small" style="left:12px;top:129px;width:266px;font-size:4.8px;line-height:1.35">Ut wisi enim ad minim veniam, quis nostrud exerci tation ullamcorper suscipit lobortis nisl ut aliquip ex ea commodo consequat. Duis autem vel eum iriure dolor in hendrerit in vulputate velit esse molestie consequat, vel illum dolore eu feugiat nulla facilisis at vero eros et accumsan et iusto odio dignissim qui blandit praesent luptatum zzril delenit augue duis dolore te feugait nulla facilisi.</div>
  <div class="footer"><span class="conf">confidential</span><div class="band">© 2015 Nordlicht Security | Ihre IT-Sicherheits-Analysten</div><div class="page">Page 01</div></div>
</section>

<!-- 18 Contact -->
<section class="slide" style="left:307px;top:866px">
  <div class="brand" style="left:128px;right:auto;top:16px;font-size:5.5px"><span class="brand-dot" style="width:13px;height:13px"></span><span>Nordlicht<br>Security</span></div>
  <div class="abs" style="left:0;right:0;top:48px;text-align:center;font-size:10px;font-weight:700;color:var(--blue-dark)">CONTACT US</div>
  <div class="abs" style="left:30px;right:30px;top:64px;text-align:center;font-size:3.6px;color:var(--blue-dark);line-height:1.35">At vero eos et accusam et justo duo dolores et ea rebum. Stet clita kasd gubergren, no sea takimata sanctus est Lorem ipsum dolor sit amet.</div>
  <div class="abs" style="left:32px;top:92px;font-size:3.6px;color:var(--blue-dark);line-height:1.5">
    <div style="font-size:5px;text-decoration:underline;margin-bottom:2px">ADDRESS</div>
    <div>Hafenstraße 12<br>20457 Hamburg<br>Deutschland</div>
    <div style="margin-top:14px"><b>PHONE</b> &nbsp;+49 40 000 0000<br><b>FAX</b> &nbsp;+49 40 000 0001<br><b>EMAIL</b> &nbsp;kontakt@nordlicht.example</div>
  </div>
  <div class="ph" role="img" aria-label="Stadtplan mit Standortmarkierung" style="left:114px;top:88px;width:146px;height:84px;background:linear-gradient(135deg,#e9e4d6,#d4dce4 60%,#f2ead0)"></div>
  <div class="abs" style="left:0;right:0;bottom:0;height:12px;background:var(--blue);display:flex;justify-content:center;gap:30px;align-items:center;font-size:4px;color:#fff">
    <span>● nordlicht.example/news</span><span>● nordlicht.example/blog</span><span>● nordlicht.example/jobs</span>
  </div>
</section>

</div>
</body>
</html>
```